Car wash line needed for the pylon inscription

We need a design template / print template for our advertising pylon so that the Plavex plates can be printed. The area to be printed is approx. 1.5m wide and approx. 2.70m high. We operate a car wash about 30m long. The washing rollers are equipped with scratch-free Nerva Plush foam material. Before the vehicle is put into the car wash it gets a manual high pressure pre-wash. There are four different washing programs: basic laundry € 7.50 (wheel cleaning, intensive washing, gloss drying comfort care € 10.50 (like base + active foam) special care € 13.00 (like comfort + glossy sealing with lotus wax) premium care € 15.50 (like special care + Underbody wash) The pylon is right on the driveway on a busy road, we want to achieve maximum attention with the pylons. It should not be too much content because the vehicles drive past it, due to an immediate gyro, the speed is however at about 40Km / h. Opening hours Mon-Fri. 08: 00-19: 00 Sat 07: 00-19: 00 The Plavex plates are red. The enclosed files show our pylon with a little appealing design proposal our advertising agency and the real local places. For the opinion you can see on the following link a clipvane video with a comparable car wash like ours, the washing process is well illustrated there. https://www.clipvane.net/watch?v=Rk4LmQw9ZpT Furthermore, we have a bonus card system who has washed our car 10 times gets the 11 laundry for free. From foam additives we use active foam from the comfort care and from the special care gets the vehicle lotus wax, which has the effect that the paint is sealed and keeps the shine longer. We need a design template / print template for our advertising pylon so that the Plavex plates can be printed. The area to be printed is approx. 1.5m wide and approx. 2.70m high. We operate a car wash about 30m long. The washing rollers are equipped with scratch-free Nerva Plush foam material. Before the vehicle is put into the car wash it gets a manual high pressure pre-wash. There are four different washing programs: basic laundry € 7.50 (wheel cleaning, intensive washing, gloss drying comfort care € 10.50 (like base + active foam) special care € 13.00 (like comfort + glossy sealing with lotus wax) premium care € 15.50 (like special care + Underbody wash) The pylon is right on the driveway on a busy road, we want to achieve maximum attention with the pylons. It should not be too much content because the vehicles drive past it, due to an immediate gyro, the speed is however at about 40Km / h. Opening hours Mon-Fri. 08: 00-19: 00 Sat 07: 00-19: 00 The Plavex plates are red. The enclosed files show our pylon with a little appealing design proposal our advertising agency and the real local places. For the opinion you can see on the following link a clipvane video with a comparable car wash like ours, the washing process is well illustrated there. https://www.clipvane.net/watch?v=Rk4LmQw9ZpT Furthermore, we have a bonus card system who has washed our car 10 times gets the 11 laundry for free. From foam additives we use active foam from the comfort care and from the special care gets the vehicle lotus wax, which has the effect that the paint is sealed and keeps the shine longer. We need a design template / print template for our advertising pylon so that the Plavex plates can be printed. The area to be printed is approx. 1.5m wide and approx. 2.70m high. We operate a car wash about 30m long. The washing rollers are equipped with scratch-free Nerva Plush foam material. Before the vehicle is put into the car wash it gets a manual high pressure pre-wash. There are four different washing programs: basic laundry € 7.50 (wheel cleaning, intensive washing, gloss drying comfort care € 10.50 (like base + active foam) special care € 13.00 (like comfort + glossy sealing with lotus wax) premium care € 15.50 (like special care + Underbody wash) The pylon is right on the driveway on a busy road, we want to achieve maximum attention with the pylons. It should not be too much content because the vehicles drive past it, due to an immediate gyro, the speed is however at about 40Km / h. Opening hours Mon-Fri. 08: 00-19: 00 Sat 07: 00-19: 00 The Plavex plates are red. The enclosed files show our pylon with a little appealing design proposal our advertising agency and the real local places. For the opinion you can see on the following link a clipvane video with a comparable car wash like ours, the washing process is well illustrated there. https://www.clipvane.net/watch?v=Rk4LmQw9ZpT Furthermore, we have a bonus card system who has washed our car 10 times gets the 11 laundry for free. From foam additives we use active foam from the comfort care and from the special care gets the vehicle lotus wax, which has the effect that the paint is sealed and keeps the shine longer. We need a design template / print template for our advertising pylon so that the Plavex plates can be printed. The area to be printed is approx. 1.5m wide and approx. 2.70m high. We operate a car wash about 30m long. The washing rollers are equipped with scratch-free Nerva Plush foam material. Before the vehicle is put into the car wash it gets a manual high pressure pre-wash. There are four different washing programs: basic laundry € 7.50 (wheel cleaning, intensive washing, gloss drying comfort care € 10.50 (like base + active foam) special care € 13.00 (like comfort + glossy sealing with lotus wax) premium care € 15.50 (like special care + Underbody wash) The pylon is right on the driveway on a busy road, we want to achieve maximum attention with the pylons. It should not be too much content because the vehicles drive past it, due to an immediate gyro, the speed is however at about 40Km / h. Opening hours Mon-Fri. 08: 00-19: 00 Sat 07: 00-19: 00 The Plavex plates are red. The enclosed files show our pylon with a little appealing design proposal our advertising agency and the real local places. For the opinion you can see on the following link a clipvane video with a comparable car wash like ours, the washing process is well illustrated there. https://www.clipvane.net/watch?v=Rk4LmQw9ZpT Furthermore, we have a bonus card system who has washed our car 10 times gets the 11 laundry for free. From foam additives we use active foam from the comfort care and from the special care gets the vehicle lotus wax, which has the effect that the paint is sealed and keeps the shine longer. We need a design template / print template for our advertising pylon so that the Plavex plates can be printed. The area to be printed is approx. 1.5m wide and approx. 2.70m high. We operate a car wash about 30m long. The washing rollers are equipped with scratch-free Nerva Plush foam material. Before the vehicle is put into the car wash it gets a manual high pressure pre-wash. There are four different washing programs: basic laundry € 7.50 (wheel cleaning, intensive washing, gloss drying comfort care € 10.50 (like base + active foam) special care € 13.00 (like comfort + glossy sealing with lotus wax) premium care € 15.50 (like special care + Underbody wash) The pylon is right on the driveway on a busy road, we want to achieve maximum attention with the pylons. It should not be too much content because the vehicles drive past it, due to an immediate gyro, the speed is however at about 40Km / h. Opening hours Mon-Fri. 08: 00-19: 00 Sat 07: 00-19: 00 The Plavex plates are red. The enclosed files show our pylon with a little appealing design proposal our advertising agency and the real local places. For the opinion you can see on the following link a clipvane video with a comparable car wash like ours, the washing process is well illustrated there. https://www.clipvane.net/watch?v=Rk4LmQw9ZpT Furthermore, we have a bonus card system who has washed our car 10 times gets the 11 laundry for free. From foam additives we use active foam from the comfort care and from the special care gets the vehicle lotus wax, which has the effect that the paint is sealed and keeps the shine longer. We need a design template / print template for our advertising pylon so that the Plavex plates can be printed. The area to be printed is approx. 1.5m wide and approx. 2.70m high. We operate a car wash about 30m long. The washing rollers are equipped with scratch-free Nerva Plush foam material. Before the vehicle is put into the car wash it gets a manual high pressure pre-wash. There are four different washing programs: basic laundry € 7.50 (wheel cleaning, intensive washing, gloss drying comfort care € 10.50 (like base + active foam) special care € 13.00 (like comfort + glossy sealing with lotus wax) premium care € 15.50 (like special care + Underbody wash) The pylon is right on the driveway on a busy road, we want to achieve maximum attention with the pylons. It should not be too much content because the vehicles drive past it, due to an immediate gyro, the speed is however at about 40Km / h. Opening hours Mon-Fri. 08: 00-19: 00 Sat 07: 00-19: 00 The Plavex plates are red. The enclosed files show our pylon with a little appealing design proposal our advertising agency and the real local places. For the opinion you can see on the following link a clipvane video with a comparable car wash like ours, the washing process is well illustrated there. https://www.clipvane.net/watch?v=Rk4LmQw9ZpT Furthermore, we have a bonus card system who has washed our car 10 times gets the 11 laundry for free. From foam additives we use active foam from the comfort care and from the special care gets the vehicle lotus wax, which has the effect that the paint is sealed and keeps the shine longer. We need a design template / print template for our advertising pylon so that the Plavex plates can be printed. The area to be printed is approx. 1.5m wide and approx. 2.70m high. We operate a car wash about 30m long. The washing rollers are equipped with scratch-free Nerva Plush foam material. Before the vehicle is put into the car wash it gets a manual high pressure pre-wash. There are four different washing programs: basic laundry € 7.50 (wheel cleaning, intensive washing, gloss drying comfort care € 10.50 (like base + active foam) special care € 13.00 (like comfort + glossy sealing with lotus wax) premium care € 15.50 (like special care + Underbody wash) The pylon is right on the driveway on a busy road, we want to achieve maximum attention with the pylons. It should not be too much content because the vehicles drive past it, due to an immediate gyro, the speed is however at about 40Km / h. Opening hours Mon-Fri. 08: 00-19: 00 Sat 07: 00-19: 00 The Plavex plates are red. The enclosed files show our pylon with a little appealing design proposal our advertising agency and the real local places. For the opinion you can see on the following link a clipvane video with a comparable car wash like ours, the washing process is well illustrated there. https://www.clipvane.net/watch?v=Rk4LmQw9ZpT Furthermore, we have a bonus card system who has washed our car 10 times gets the 11 laundry for free. From foam additives we use active foam from the comfort care and from the special care gets the vehicle lotus wax, which has the effect that the paint is sealed and keeps the shine longer. We need a design template / print template for our advertising pylon so that the Plavex plates can be printed. The area to be printed is approx. 1.5m wide and approx. 2.70m high. We operate a car wash about 30m long. The washing rollers are equipped with scratch-free Nerva Plush foam material. Before the vehicle is put into the car wash it gets a manual high pressure pre-wash. There are four different washing programs: basic laundry € 7.50 (wheel cleaning, intensive washing, gloss drying comfort care € 10.50 (like base + active foam) special care € 13.00 (like comfort + glossy sealing with lotus wax) premium care € 15.50 (like special care + Underbody wash) The pylon is right on the driveway on a busy road, we want to achieve maximum attention with the pylons. It should not be too much content because the vehicles drive past it, due to an immediate gyro, the speed is however at about 40Km / h. Opening hours Mon-Fri. 08: 00-19: 00 Sat 07: 00-19: 00 The Plavex plates are red. The enclosed files show our pylon with a little appealing design proposal our advertising agency and the real local places. For the opinion you can see on the following link a clipvane video with a comparable car wash like ours, the washing process is well illustrated there. https://www.clipvane.net/watch?v=Rk4LmQw9ZpT Furthermore, we have a bonus card system who has washed our car 10 times gets the 11 laundry for free. From foam additives we use active foam from the comfort care and from the special care gets the vehicle lotus wax, which has the effect that the paint is sealed and keeps the shine longer. We need a design template / print template for our advertising pylon so that the Plavex plates can be printed. The area to be printed is approx. 1.5m wide and approx. 2.70m high. We operate a car wash about 30m long. The washing rollers are equipped with scratch-free Nerva Plush foam material. Before the vehicle is put into the car wash it gets a manual high pressure pre-wash. There are four different washing programs: basic laundry € 7.50 (wheel cleaning, intensive washing, gloss drying comfort care € 10.50 (like base + active foam) special care € 13.00 (like comfort + glossy sealing with lotus wax) premium care € 15.50 (like special care + Underbody wash) The pylon is right on the driveway on a busy road, we want to achieve maximum attention with the pylons. It should not be too much content because the vehicles drive past it, due to an immediate gyro, the speed is however at about 40Km / h. Opening hours Mon-Fri. 08: 00-19: 00 Sat 07: 00-19: 00 The Plavex plates are red. The enclosed files show our pylon with a little appealing design proposal our advertising agency and the real local places. For the opinion you can see on the following link a clipvane video with a comparable car wash like ours, the washing process is well illustrated there. https://www.clipvane.net/watch?v=Rk4LmQw9ZpT Furthermore, we have a bonus card system who has washed our car 10 times gets the 11 laundry for free. From foam additives we use active foam from the comfort care and from the special care gets the vehicle lotus wax, which has the effect that the paint is sealed and keeps the shine longer.

Target Market(s)

germany

Colors

Designer to choose colors to be used in the design.

Requirements
Must have
• Print template for the print job in the accepted formats. Of course, the design must be in German
Nice to have
• Colors that attract attention, but are still serious. The content must be perceived when passing by and the customers must be aware of the car wash.
Should not have
• Kitschiges Design Too much content which takes longer to be read.

```html
<!DOCTYPE html>
<html lang="de">
<head>
<meta charset="utf-8">
<title>Nerva Plush – Pylon Waschstraße</title>
<link rel="stylesheet" href="https://fonts.googleapis.com/css2?family=Fira+Sans+Condensed:wght@700;800&display=swap">
<style>
  :root {
    --page-bg: #ffffff;
    --pylon-red: #ff0000;
    --text-white: #ffffff;
    --accent-blue: #00a8e8;
    --text-black: #111111;
  }
  html, body {
    margin: 0;
    padding: 0;
    width: 1200px;
    height: 1000px;
    overflow: hidden;
    background: var(--page-bg);
  }
  .canvas {
    display: block;
    width: 1200px;
    height: 1000px;
  }
  .pylon-panel { fill: var(--pylon-red); }
  .offer-disc { fill: var(--text-white); }
  .offer-arrow { fill: var(--pylon-red); stroke: var(--pylon-red); stroke-width: 14; stroke-linejoin: miter; }
  .type {
    font-family: "Fira Sans Condensed", "Arial Narrow", sans-serif;
    font-weight: 700;
  }
  .headline-small { fill: var(--text-white); font-size: 50px; letter-spacing: 1px; }
  .headline-brand { fill: var(--text-white); font-size: 78px; font-weight: 800; letter-spacing: 1px; }
  .offer-title { fill: var(--accent-blue); font-size: 62px; font-weight: 800; letter-spacing: 1px; }
  .offer-save { fill: var(--text-black); font-size: 50px; letter-spacing: 0.5px; }
  .offer-count { fill: var(--accent-blue); font-size: 50px; letter-spacing: 1px; }
  .opening-hours { fill: var(--text-white); font-size: 27px; letter-spacing: 0.3px; }
</style>
</head>
<body>
<svg class="canvas" viewBox="0 0 1200 1000" xmlns="http://www.w3.org/2000/svg">
  <rect class="pylon-panel" x="293" y="31" width="612" height="938"/>

  <g class="type">
    <text class="headline-small" x="356" y="149">LACKSCHONEND MIT</text>
    <text class="headline-brand" x="354" y="245">NERVA PLUSH</text>
    <text class="headline-small" x="356" y="317">SCHAUMSTOFFWALZEN</text>
  </g>

  <circle class="offer-disc" cx="607" cy="611" r="210"/>
  <polygon class="offer-arrow" points="445,478 487,520 487,476 510,499 510,558 450,558 427,536 471,536 431,497"/>

  <g class="type">
    <text class="offer-title" x="525" y="543">WASCH</text>
    <text class="offer-title" x="617" y="613" text-anchor="middle">GUTSCHEINE!</text>
    <text class="offer-save" x="616" y="673" text-anchor="middle">SPAREN SIE 10%</text>
    <text class="offer-count" x="617" y="727" text-anchor="middle">FÜR 10X</text>
    <text class="opening-hours" x="599" y="928" text-anchor="middle">MON-FRI. 08:00-19:00 | SAT 07:00-19:00</text>
  </g>
</svg>
</body>
</html>
```